Four in One (Flexible infographic for Content Management Industry)

See attachment.
A graphic depicting 4 products, where each can stand on its own and each can be combined with others, but where, if all are taken together, the best result is achieved (the "super product").
Intended use is web. See attached file as an example.
The most basic idea is as the attached diagram shows, where 4 rectangles are arranged in a quadrangle, with a middle rectangle in the center representing the combined 4 products. This concept is fine except it is a bit too obvious as it stands. We are looking for either a variation of this or another concept.
The audience is technical + professional + enterprise - NOT consumers. Hence the design should be conservative in nature.
We are aware of tools like as Canva or Pictogram where such graphics are available, but we are looking for something with a bit more imagination and flexibility.
This graphic should be targeted to web sites and be delivered with vector-based (SVG) graphics.

```html
<!DOCTYPE html>
<html lang="en">
<head>
<meta charset="utf-8">
<title>Four in One – Super Product Matrix</title>
<link href="https://fonts.googleapis.com/css2?family=Montserrat:wght@800&family=Open+Sans:wght@400&display=swap" rel="stylesheet">
<style>
  :root {
    --bg: #ffffff;
    --axis: #cdd1da;
    --axis-text: #ffffff;
    --connector: #c3c8d2;
    --card: #f7f8fb;
    --inner-a: #e3e7f0;
    --inner-b: #fbfcfe;
    --body-text: #545963;
    --center-text: #1d1f24;
    --blue-a: #0a86cb;
    --blue-b: #3d5ea9;
    --teal-a: #14c2d8;
    --teal-b: #0ea3c2;
    --purple-a: #7651a6;
    --purple-b: #c34e97;
    --pink-a: #e3579f;
    --pink-b: #d55aa8;
  }
  html, body {
    margin: 0;
    padding: 0;
    width: 1200px;
    height: 847px;
    overflow: hidden;
    background: var(--bg);
  }
  .matrix {
    display: block;
    width: 1200px;
    height: 847px;
  }
  .axis-shape { fill: var(--axis); }
  .axis-label {
    font-family: "Montserrat", sans-serif;
    font-weight: 800;
    font-size: 40px;
    fill: var(--axis-text);
    text-anchor: middle;
  }
  .connector { fill: var(--connector); }
  .card { fill: var(--card); filter: drop-shadow(0 6px 10px rgba(90, 100, 125, 0.22)); }
  .card-inner { fill: url(#innerFill); }
  .badge-number {
    font-family: "Open Sans", sans-serif;
    font-weight: 400;
    font-size: 50px;
    fill: #ffffff;
    text-anchor: middle;
  }
  .card-title {
    font-family: "Montserrat", sans-serif;
    font-weight: 800;
    font-size: 37px;
    text-anchor: middle;
  }
  .title-blue { fill: var(--blue-a); }
  .title-teal { fill: var(--teal-a); }
  .title-purple { fill: url(#purpleFill); }
  .title-pink { fill: var(--pink-a); }
  .card-body {
    font-family: "Open Sans", sans-serif;
    font-weight: 400;
    font-size: 19.5px;
    letter-spacing: 0.8px;
    fill: var(--body-text);
    text-anchor: middle;
  }
  .center-card { fill: var(--card); filter: drop-shadow(0 4px 8px rgba(90, 100, 125, 0.25)); }
  .center-label {
    font-family: "Open Sans", sans-serif;
    font-weight: 400;
    font-size: 42px;
    fill: var(--center-text);
    text-anchor: middle;
  }
</style>
</head>
<body>
<svg class="matrix" viewBox="0 0 2287 1614" xmlns="http://www.w3.org/2000/svg" role="img" aria-label="Four products arranged in a matrix around a combined super product">
  <defs>
    <linearGradient id="innerFill" x1="0" y1="0" x2="1" y2="1">
      <stop offset="0" stop-color="var(--inner-a)"/>
      <stop offset="1" stop-color="var(--inner-b)"/>
    </linearGradient>
    <linearGradient id="blueFill" x1="0" y1="0" x2="1" y2="0">
      <stop offset="0" stop-color="var(--blue-a)"/>
      <stop offset="1" stop-color="var(--blue-b)"/>
    </linearGradient>
    <linearGradient id="tealFill" x1="0" y1="0" x2="1" y2="1">
      <stop offset="0" stop-color="var(--teal-a)"/>
      <stop offset="1" stop-color="var(--teal-b)"/>
    </linearGradient>
    <linearGradient id="purpleFill" x1="0" y1="0" x2="1" y2="0">
      <stop offset="0" stop-color="var(--purple-a)"/>
      <stop offset="1" stop-color="var(--purple-b)"/>
    </linearGradient>
    <linearGradient id="pinkFill" x1="0" y1="0" x2="1" y2="1">
      <stop offset="0" stop-color="var(--pink-a)"/>
      <stop offset="1" stop-color="var(--pink-b)"/>
    </linearGradient>
  </defs>

  <g transform="translate(0 7)">
    <!-- Axes -->
    <g class="axes">
      <path class="axis-shape" d="M499 768 V238 L531 200 L563 238 V768 Z"/>
      <path class="axis-shape" d="M499 803 V1330 L531 1368 L563 1330 V803 Z"/>
      <path class="axis-shape" d="M1180 1408 H644 L609 1440 L644 1472 H1180 Z"/>
      <path class="axis-shape" d="M1213 1408 H1742 L1777 1440 L1742 1472 H1213 Z"/>
      <text class="axis-label" transform="translate(541 517) rotate(-90)">Lorem Ipsum</text>
      <text class="axis-label" transform="translate(541 1077) rotate(-90)">Lorem Ipsum</text>
      <text class="axis-label" x="900" y="1452">Lorem Ipsum</text>
      <text class="axis-label" x="1461" y="1452">Lorem Ipsum</text>
    </g>

    <!-- Connectors -->
    <rect class="connector" x="1182" y="286" width="31" height="994"/>
    <rect class="connector" x="700" y="762" width="995" height="28"/>

    <!-- Corner accents -->
    <rect x="596" y="178" width="179" height="179" rx="14" fill="url(#blueFill)"/>
    <rect x="1620" y="178" width="179" height="179" rx="14" fill="url(#tealFill)"/>
    <rect x="596" y="1197" width="179" height="179" rx="14" fill="url(#purpleFill)"/>
    <rect x="1618" y="1197" width="179" height="179" rx="14" fill="url(#pinkFill)"/>

    <!-- Card 01 -->
    <g class="quadrant">
      <rect class="card" x="616" y="196" width="566" height="566" rx="18"/>
      <rect class="card-inner" x="632" y="212" width="535" height="535" rx="60"/>
      <circle cx="900" cy="329" r="57" fill="url(#blueFill)"/>
      <text class="badge-number" x="900" y="347">01</text>
      <text class="card-title title-blue" x="898" y="458">Title Here</text>
      <text class="card-body" x="898" y="523">Lorem ipsum dolor sit amet,</text>
      <text class="card-body" x="898" y="553">consectetuer adipiscing elit, sed</text>
      <text class="card-body" x="898" y="583">diam nonummy nibh euismod</text>
      <text class="card-body" x="898" y="613">tincidunt ut laoreet dolore</text>
      <text class="card-body" x="898" y="643">magna aliquam erat volutpat.</text>
    </g>

    <!-- Card 02 -->
    <g class="quadrant">
      <rect class="card" x="1213" y="196" width="566" height="566" rx="18"/>
      <rect class="card-inner" x="1228" y="212" width="535" height="535" rx="60"/>
      <circle cx="1495" cy="329" r="57" fill="url(#tealFill)"/>
      <text class="badge-number" x="1495" y="347">02</text>
      <text class="card-title title-teal" x="1495" y="458">Title Here</text>
      <text class="card-body" x="1495" y="523">Lorem ipsum dolor sit amet,</text>
      <text class="card-body" x="1495" y="553">consectetuer adipiscing elit, sed</text>
      <text class="card-body" x="1495" y="583">diam nonummy nibh euismod</text>
      <text class="card-body" x="1495" y="613">tincidunt ut laoreet dolore</text>
      <text class="card-body" x="1495" y="643">magna aliquam erat volutpat.</text>
    </g>

    <!-- Card 03 -->
    <g class="quadrant">
      <rect class="card" x="616" y="790" width="566" height="566" rx="18"/>
      <rect class="card-inner" x="632" y="806" width="535" height="535" rx="60"/>
      <circle cx="900" cy="931" r="51" fill="url(#purpleFill)"/>
      <text class="badge-number" x="900" y="949">03</text>
      <text class="card-title title-purple" x="898" y="1060">Title Here</text>
      <text class="card-body" x="898" y="1125">Lorem ipsum dolor sit amet,</text>
      <text class="card-body" x="898" y="1155">consectetuer adipiscing elit, sed</text>
      <text class="card-body" x="898" y="1185">diam nonummy nibh euismod</text>
      <text class="card-body" x="898" y="1215">tincidunt ut laoreet dolore</text>
      <text class="card-body" x="898" y="1245">magna aliquam erat volutpat.</text>
    </g>

    <!-- Card 04 -->
    <g class="quadrant">
      <rect class="card" x="1213" y="790" width="566" height="566" rx="18"/>
      <rect class="card-inner" x="1228" y="806" width="535" height="535" rx="60"/>
      <circle cx="1498" cy="931" r="51" fill="url(#pinkFill)"/>
      <text class="badge-number" x="1498" y="949">04</text>
      <text class="card-title title-pink" x="1495" y="1060">Title Here</text>
      <text class="card-body" x="1495" y="1125">Lorem ipsum dolor sit amet,</text>
      <text class="card-body" x="1495" y="1155">consectetuer adipiscing elit, sed</text>
      <text class="card-body" x="1495" y="1185">diam nonummy nibh euismod</text>
      <text class="card-body" x="1495" y="1215">tincidunt ut laoreet dolore</text>
      <text class="card-body" x="1495" y="1245">magna aliquam erat volutpat.</text>
    </g>

    <!-- Super product hub -->
    <g class="hub">
      <rect x="1051" y="631" width="131" height="146" rx="4" fill="url(#blueFill)"/>
      <rect x="1211" y="631" width="131" height="146" rx="4" fill="url(#tealFill)"/>
      <rect x="1051" y="791" width="131" height="130" rx="4" fill="url(#purpleFill)"/>
      <rect x="1211" y="791" width="131" height="130" rx="4" fill="url(#pinkFill)"/>
      <rect class="center-card" x="1068" y="648" width="259" height="259" rx="10"/>
      <rect class="card-inner" x="1084" y="664" width="227" height="227" rx="40"/>
      <text class="center-label" x="1196" y="762">Super</text>
      <text class="center-label" x="1196" y="815">Product</text>
    </g>
  </g>
</svg>
</body>
</html>
```